BRANDHILL real estate family office

Hello, Our business is a real estate intermediation activity on high-end goods (amounts exceeding € 10m) for corporate and private clients. You can see our logo on the site www.brandhill-demo.fr We would like to keep that spirit with the hexagon that represents France (transactions between Monaco and Saint Tropez, Courchevel and Paris). And the "baseline" that is "real estate family office". The corporate logo should be and can be printed by embossing (relief). We must integrate the name, first name, phone, email and website. Finally, to imbibe the spirit of business, here is a detail of the activity. "Genuine consulting firm in real estate investments, BRANDHILL works with its customers as a specialized player in the high-end markets, we are recognized for our ultra-confidential approach and tailor-made, as well as the quality of our network. We broadcast any information on the market and we work exclusively through a strong relationship we have developed over the years. BRANDHILL is active on the French Riviera (from Monaco to Saint-Tropez), the Alps (Courchevel, Méribel, Megève) and Paris (essentially market premium). Always looking for opportunities for our clients, we work on two investment areas: residential luxury real estate (properties, vineyards, mansions, land, etc.) commercial real estate (empty office buildings or yield, hotel properties, land, etc.) "

Target Market(s)

High foreign end customers. corporate and private.

Industry/Entity Type

Real Estate

Contact Information for Business Card

LOGO
baseline
Laurent Dufossé
+33(0)6.41.57.09.64
ld@brandhill-demo.fr
www.brandhill-demo.fr

Font styles to use
Serif

Colors
cedeed
0255a3
3277b5
85abd2
85cae6
34a7d7
0792cd
cfdeed
1b1b1b

Requirements
Must have
• see description

```html
<!DOCTYPE html>
<html lang="en">
<head>
<meta charset="utf-8">
<title>BRANDHILL – business card</title>
<link rel="stylesheet" href="https://fonts.googleapis.com/css2?family=Jost:wght@400;500&display=swap">
<style>
  :root {
    --navy: #233d8a;
    --navy-deep: #1d3478;
    --grey-logo: #6e6f73;
    --grey-band: #7c7d81;
    --white: #ffffff;
    --paper: #f4f4f4;
    --backdrop: #e4e6ea;
    --tagline: #2c4a9a;
  }
  html, body {
    margin: 0;
    padding: 0;
    width: 1200px;
    height: 892px;
    overflow: hidden;
    background: var(--backdrop);
    font-family: "Jost", Arial, sans-serif;
  }
  .canvas {
    position: relative;
    width: 1200px;
    height: 892px;
  }
  .card {
    position: absolute;
    left: 280px;
    width: 640px;
    height: 366px;
    border-radius: 22px;
    overflow: hidden;
    box-shadow: 0 6px 18px rgba(0,0,0,0.18);
  }
  .card--front { top: 50px; background: var(--white); }
  .card--back  { top: 476px; background: linear-gradient(135deg, var(--white), var(--paper)); }

  .card__wave {
    position: absolute;
    inset: 0;
    width: 100%;
    height: 100%;
  }

  .brand {
    position: absolute;
    text-align: right;
  }
  .brand__name {
    display: block;
    font-weight: 400;
    color: var(--grey-logo);
    letter-spacing: 0.08em;
    line-height: 1;
  }
  .brand__tagline {
    display: block;
    color: var(--tagline);
    letter-spacing: 0.12em;
    margin-top: 4px;
  }
  .card--front .brand { left: 110px; top: 26px; }
  .card--front .brand__name { font-size: 62px; }
  .card--front .brand__tagline { font-size: 18px; }

  .card--back .brand { left: 90px; top: 128px; }
  .card--back .brand__name { font-size: 76px; }
  .card--back .brand__tagline { font-size: 21px; }

  .holder {
    position: absolute;
    left: 34px;
    top: 240px;
    margin: 0;
    font-size: 24px;
    font-weight: 400;
    color: var(--white);
  }
  .divider {
    position: absolute;
    left: 300px;
    top: 232px;
    width: 3px;
    height: 108px;
    background: var(--white);
  }
  .contacts {
    position: absolute;
    left: 330px;
    top: 234px;
    margin: 0;
    padding: 0;
    list-style: none;
  }
  .contacts__item {
    display: flex;
    align-items: center;
    gap: 14px;
    height: 34px;
    font-size: 19px;
    color: var(--white);
  }
  .contacts__icon {
    width: 22px;
    height: 18px;
    background: var(--white);
    display: flex;
    align-items: center;
    justify-content: center;
    flex: none;
  }
</style>
</head>
<body>
<main class="canvas">

  <section class="card card--front" aria-label="Card front">
    <svg class="card__wave" viewBox="0 0 640 366" preserveAspectRatio="none" aria-hidden="true">
      <path d="M0,124 C160,146 320,162 440,168 C540,174 600,186 640,198 L640,366 L0,366 Z" fill="var(--grey-band)"/>
      <path d="M0,142 C160,164 320,180 440,186 C540,192 600,204 640,216 L640,366 L0,366 Z" fill="var(--white)"/>
      <path d="M0,147 C160,169 320,185 440,191 C540,197 600,209 640,221 L640,366 L0,366 Z" fill="var(--navy)"/>
    </svg>

    <div class="brand">
      <span class="brand__name">BRANDHILL</span>
      <span class="brand__tagline">real estate family office</span>
    </div>

    <h1 class="holder">Laurent Dufossé</h1>
    <div class="divider"></div>

    <ul class="contacts">
      <li class="contacts__item">
        <span class="contacts__icon">
          <svg width="12" height="12" viewBox="0 0 12 12" aria-hidden="true">
            <path d="M2,1 L4,1 L5,3.5 L3.8,4.6 C4.5,6 5.8,7.4 7.3,8.2 L8.5,7 L11,8 L11,10 C11,10.6 10.5,11 10,11 C5,10.6 1.4,7 1,2 C1,1.4 1.4,1 2,1 Z" fill="var(--navy)"/>
          </svg>
        </span>
        <span>+33(0)6.41.57.09.64</span>
      </li>
      <li class="contacts__item">
        <span class="contacts__icon">
          <svg width="13" height="13" viewBox="0 0 14 14" aria-hidden="true">
            <circle cx="7" cy="7" r="6" fill="var(--navy)"/>
            <ellipse cx="7" cy="7" rx="2.6" ry="6" fill="none" stroke="var(--white)" stroke-width="1"/>
            <line x1="1" y1="7" x2="13" y2="7" stroke="var(--white)" stroke-width="1"/>
          </svg>
        </span>
        <span>www.brandhill-demo.fr</span>
      </li>
      <li class="contacts__item">
        <span class="contacts__icon">
          <svg width="14" height="10" viewBox="0 0 14 10" aria-hidden="true">
            <rect x="0.5" y="0.5" width="13" height="9" fill="none" stroke="var(--navy)" stroke-width="1.2"/>
            <path d="M0.5,0.5 L7,6 L13.5,0.5" fill="none" stroke="var(--navy)" stroke-width="1.2"/>
          </svg>
        </span>
        <span>ld@brandhill-demo.fr</span>
      </li>
    </ul>
  </section>

  <section class="card card--back" aria-label="Card back">
    <div class="brand">
      <span class="brand__name">BRANDHILL</span>
      <span class="brand__tagline">real estate family office</span>
    </div>
  </section>

</main>
</body>
</html>
```